Flyer Vacation Gift Certificate

I need to create a beautiful flyer 8.5 x 11 PDF format flyer design. <br/><br/>Instructions:<br/>The flyer will really be a gift voucher for a las vegas vacation getaway. So must have a Las Vegas Theme exciting fun<br/><br/>The voucher should have two modules that will be editable. <br/>Must have a "Compliments Of" area and also must have an "Exclusively For" area<br/><br/>Keep in mind that this flyer will be printed so keep that in mind :)<br/><br/>Here the is the content for the vacation voucher:<br/><br/>There is no doubt that Las Vegas is one of the hottest travel destinations around the world. In fact, some people would even go as far as<br/>saying that perhaps it is THE hottest place to visit. Enjoy up to 4 nights of resort/casino accommodations in exciting Las Vegas, NV. Millions of people travel to this exciting city each year to enjoy its thrills. Thanks to the business you received this certificate from, now you can enjoy exciting Las Vegas, NV too!<br/><br/>Features:<br/>*Travel 7 Days A Week<br/>*Stay Your Choice Of Nights (1-4 Nights)<br/>*Good For Two Adults & Two Children<br/>*Pay Just The Taxes & Fees<br/>*Multiple Travel Date Requests Allowed<br/>*Fully Transferable To Another Person<br/>*Just A 30 Days Advance Notice Required<br/>*You Will Have 12 Months To Complete Travel After Redemption<br/><br/>HOW CAN WE DO THIS?<br/><br/>We contract with the world leading hotel chains and resorts to help them fill their otherwise empty rooms.<br/><br/>We help fill empty rooms which the hotels, resorts and cruise lines turn into additional revenue from other areas of their property and future bookings.<br/><br/>Hotels rarely experience full occupancy, yet they remain open, providing rooms and services at fixed costs. So when hotels give out their rooms by partnering with marketing companies like us, they might miss out on the room fee, but they already didn't have that in the first place, at least now they have the opportunity to gain a customer for their in-house restaurants, room service, their casinos, an extra day stay, future bookings, etc.<br/><br/>VIEW ALL THE DETAILS OF THIS SPECIAL OFFER AND REDEEM ONLINE AT <br/>WWW.TOPAZVOUCHERDESK.COM<br/><br/>Certificate ID # 47261-38504<br/>Expires 02/29/2020<br/><br/><br/>*terms and conditions apply see website for details<br/><br/>KEEP IN MIND THE EXAMPLES I AM UPLOADING ARE SIMPLY TO SHOW YOU THAT THEY CONTAIN THE "COMPLIMENTS OF" AND "EXCLUSIVELY FOR" ELEMENTS. THESE MUST BE INCLUDED IN NEW DESIGN. PLEASE ONLY USE THE CONTENT I PROVIDED IN BRIEF, DONT USE CONTENT FROM EXAMPLES.

Target Market(s)

CONSUMERS THAT HAVE BEEN REWARDED WITH A VACATION CERTIFICATE FOR DOING BUSINESS WITH A COMPANY.

COMPANIES USE THESE AS MARKETING INCENTIVES TO ATTRACT MORE CUSTOMERS AND TO REWARD LOYALTY, ETC.

Industry/Entity Type

Travel Industry

Colors

Designer to choose colors to be used in the design.

Requirements
Must have
• I need to create a beautiful flyer 8.5 x 11 PDF format flyer design.
• Instructions:
• The flyer will really be a gift voucher for a las vegas vacation getaway. So must have a Las Vegas Theme exciting fun
• The voucher should have two modules that will be editable.
• Must have a "Compliments Of" area and also must have an "Exclusively For" area
• Keep in mind that this flyer will be printed so keep that in mind :)
• Here the is the content for the vacation voucher:
• There is no doubt that Las Vegas is one of the hottest travel destinations around the world. In fact, some people would even go as far as
• saying that perhaps it is THE hottest place to visit. Enjoy up to 4 nights of resort/casino accommodations in exciting Las Vegas, NV. Millions of people travel to this exciting city each year to enjoy its thrills. Thanks to the business you received this certificate from, now you can enjoy exciting Las Vegas, NV too!
• Features:
• *Travel 7 Days A Week
• *Stay Your Choice Of Nights (1-4 Nights)
• *Good For Two Adults & Two Children
• *Pay Just The Taxes & Fees
• *Multiple Travel Date Requests Allowed
• *Fully Transferable To Another Person
• *Just A 30 Days Advance Notice Required
• *You Will Have 12 Months To Complete Travel After Redemption
• HOW CAN WE DO THIS?
• We contract with the world leading hotel chains and resorts to help them fill their otherwise empty rooms.
• We help fill empty rooms which the hotels, resorts and cruise lines turn into additional revenue from other areas of their property and future bookings.
• Hotels rarely experience full occupancy, yet they remain open, providing rooms and services at fixed costs. So when hotels give out their rooms by partnering with marketing companies like us, they might miss out on the room fee, but they already didn't have that in the first place, at least now they have the opportunity to gain a customer for their in-house restaurants, room service, their casinos, an extra day stay, future bookings, etc.
• VIEW ALL THE DETAILS OF THIS SPECIAL OFFER AND REDEEM ONLINE AT
• WWW.TOPAZVOUCHERDESK.COM
• Certificate ID # 47261-38504
• Expires 02/29/2020
• *terms and conditions apply see website for details
• KEEP IN MIND THE EXAMPLES I AM UPLOADING ARE SIMPLY TO SHOW YOU THAT THEY CONTAIN THE "COMPLIMENTS OF" AND "EXCLUSIVELY FOR" ELEMENTS. THESE MUST BE INCLUDED IN NEW DESIGN. PLEASE ONLY USE THE CONTENT I PROVIDED IN BRIEF, DONT USE CONTENT FROM EXAMPLES.
Nice to have
• EXCITING LAS VEGAS IMAGES THAT MAKE SOMEONE WANT TO GO THERE

```html
<!DOCTYPE html>
<html lang="en">
<head>
<meta charset="utf-8">
<title>Las Vegas Vacation Gift Certificate</title>
<link href="https://fonts.googleapis.com/css2?family=Montserrat:wght@400;500;600;700;800&display=swap" rel="stylesheet">
<style>
  :root{
    --stage:#c9cacc;
    --navy:#1b1f33;
    --navy-deep:#141727;
    --ink:#1d2236;
    --cyan:#3cc6df;
    --cyan-bright:#4fd6ee;
    --pink:#e0489b;
    --paper:#ffffff;
    --muted:#b9bfd3;
    --body:#d9ddea;
  }
  *{box-sizing:border-box;margin:0;padding:0}
  html,body{width:1200px;height:960px;overflow:hidden}
  body{background:var(--stage);font-family:"Montserrat",sans-serif;position:relative}
  .flyer{
    position:absolute;left:252px;top:30px;width:696px;height:900px;
    background:linear-gradient(180deg,var(--navy) 0%,var(--navy-deep) 100%);
    overflow:hidden;box-shadow:0 10px 30px rgba(0,0,0,.25);
  }
  .top-band{position:absolute;left:0;top:0;width:100%;height:22px;background:var(--navy-deep)}
  .city-photo{
    position:absolute;left:0;top:22px;width:100%;height:540px;
    background:
      radial-gradient(ellipse at 60% 85%,rgba(255,170,80,.55) 0%,rgba(255,120,60,0) 45%),
      radial-gradient(ellipse at 25% 70%,rgba(90,160,255,.45) 0%,rgba(90,160,255,0) 40%),
      linear-gradient(180deg,#1a1a44 0%,#2b2a6a 35%,#3a3f86 60%,#3b4f8f 78%,#263456 100%);
    clip-path:polygon(0 0,100% 0,100% 100%,0 81%);
  }
  .divider{position:absolute;left:0;top:0;width:100%;height:100%;pointer-events:none}
  .exclusive-box{
    position:absolute;left:40px;top:0;width:300px;height:72px;
    background:var(--paper);border-radius:0 0 12px 12px;padding:14px 18px;
  }
  .box-label{font-size:10px;font-weight:800;letter-spacing:.06em;color:var(--ink);text-transform:uppercase}
  .compliments-box{
    position:absolute;right:30px;top:44px;width:262px;height:136px;
    background:var(--paper);border-radius:12px;padding:16px 18px;text-align:right;color:var(--ink);
  }
  .compliments-box .box-label{font-size:12px;line-height:1.2}
  .courtesy{margin-top:14px;font-size:13px;font-weight:700;line-height:1.35}
  .intro{
    position:absolute;right:30px;top:200px;width:400px;text-align:right;
    font-size:11px;line-height:1.6;color:var(--body);
  }
  .features{
    position:absolute;left:30px;top:400px;width:300px;height:262px;
    background:var(--cyan);border-radius:16px;padding:18px 20px;color:var(--ink);
  }
  .features h2{font-size:17px;font-weight:700;color:var(--paper);margin-bottom:8px}
  .features ul{list-style:none}
  .features li{font-size:11px;line-height:1.55;font-weight:500}
  .features li::before{content:"• "}
  .how{position:absolute;left:352px;top:580px;width:318px;color:var(--body)}
  .how h2{font-size:17px;font-weight:800;color:var(--cyan-bright);margin-bottom:6px}
  .how p{font-size:10.4px;line-height:1.5}
  .redeem{
    position:absolute;left:30px;top:700px;width:310px;text-align:center;
    font-size:10px;line-height:1.6;color:var(--muted);
  }
  .redeem .url{color:var(--cyan-bright);font-weight:700}
  .terms{position:absolute;left:30px;bottom:22px;font-size:8.5px;color:var(--muted);font-style:normal}
</style>
</head>
<body>
  <article class="flyer">
    <div class="top-band"></div>
    <div class="city-photo" role="img" aria-label="Night view of the Las Vegas skyline with lit towers and busy highways"></div>
    <svg class="divider" viewBox="0 0 696 900" aria-hidden="true">
      <defs>
        <linearGradient id="glowLine" x1="0" x2="1" y1="0" y2="0">
          <stop offset="0" stop-color="#e0489b"/>
          <stop offset="1" stop-color="#3cc6df"/>
        </linearGradient>
      </defs>
      <line x1="0" y1="459" x2="696" y2="562" stroke="url(#glowLine)" stroke-width="3"/>
    </svg>

    <div class="exclusive-box"><p class="box-label">Exclusively For</p></div>

    <div class="compliments-box">
      <p class="box-label">This Certificate Is<br>Compliments Of</p>
      <p class="courtesy">Certificate Courtesy Of<br>Text Line 2<br>Text Line 3</p>
    </div>

    <p class="intro">There is no doubt that Las Vegas is one of the hottest travel destinations around the world. In fact, some people would even go as far as saying that perhaps it is THE hottest place to visit. Enjoy up to 4 nights of resort/casino accommodations in exciting Las Vegas, NV. Millions of people travel to this exciting city each year to enjoy its thrills. Thanks to the business you received this certificate from, now you can enjoy exciting Las Vegas, NV too!</p>

    <section class="features">
      <h2>Features:</h2>
      <ul>
        <li>Travel 7 Days A Week</li>
        <li>Stay Your Choice Of Nights (1-4 Nights)</li>
        <li>Good For Two Adults &amp; Two Children</li>
        <li>Pay Just The Taxes &amp; Fees</li>
        <li>Multiple Travel Date Requests Allowed</li>
        <li>Fully Transferable To Another Person</li>
        <li>Just A 30 Days Advance Notice Required</li>
        <li>You Will Have 12 Months To Complete Travel After Redemption</li>
      </ul>
    </section>

    <section class="how">
      <h2>HOW CAN WE DO THIS?</h2>
      <p>We contract with the world leading hotel chains and resorts to help them fill their otherwise empty rooms. We help fill empty rooms which the hotels, resorts and cruise lines turn into additional revenue from other areas of their property and future bookings. Hotels rarely experience full occupancy, yet they remain open, providing rooms and services at fixed costs. So when hotels give out their rooms by partnering with marketing companies like us, they might miss out on the room fee, but they already didn't have that in the first place, at least now they have the opportunity to gain a customer for their in-house restaurants, room service, their casinos, an extra day stay, future bookings, etc.</p>
    </section>

    <footer class="redeem">
      <p>VIEW ALL THE DETAILS OF THIS SPECIAL OFFER AND REDEEM ONLINE AT</p>
      <p class="url">WWW.TOPAZVOUCHERDESK.COM</p>
      <p>Certificate ID # 47261-38504</p>
      <p>Expires 02/29/2020</p>
    </footer>
  </article>
</body>
</html>
```